Business Card Design

We would like a business card that utilizes our current logo and keeps with the same feel - elegant and organic. Our farm isn't about mass production, it's about excellence, education, beautiful events and flowers - people, culture, and community.

Target Market(s)

Patrons to our farm who are interested in weddings, events, or our flowers and vegetables.

Contact Information for Business Card

Name, address, cell email (Danielle Hoskins, 2716 Wrenfield Rd, Fernbrook, CO 80742, cell 30.412.6638, email danielle@wrenfieldacres.com)

```html
<!DOCTYPE html>
<html lang="en">
<head>
<meta charset="utf-8">
<title>Wrenfield Acres — Business Card</title>
<link href="https://fonts.googleapis.com/css2?family=Lato:wght@400;700&display=swap" rel="stylesheet">
<style>
  :root {
    --backdrop: #222822;
    --card-white: #ffffff;
    --sage: #778a76;
    --gold: #a67f55;
    --ink: #4a4a4a;
  }
  * { margin: 0; padding: 0; box-sizing: border-box; }
  html, body {
    width: 1200px;
    height: 1200px;
    overflow: hidden;
    background: var(--backdrop);
    font-family: "Lato", sans-serif;
  }
  .card {
    position: absolute;
    left: 239px;
    width: 722px;
    height: 412px;
    border-radius: 19px;
    overflow: hidden;
  }
  .card--front { top: 140px; background: var(--card-white); }
  .card--back { top: 644px; background: var(--sage); }

  .sprig {
    position: absolute;
    border-radius: 0 60% 60% 0 / 0 50% 50% 0;
  }
  .card--front .sprig {
    left: 0; top: 43px; width: 283px; height: 137px;
    background: linear-gradient(100deg, rgba(119,138,118,0.15), rgba(119,138,118,0.45) 55%, rgba(119,138,118,0.1));
  }
  .card--back .sprig {
    left: 0; top: 39px; width: 360px; height: 131px;
    background: linear-gradient(100deg, rgba(255,255,255,0.08), rgba(255,255,255,0.35) 55%, rgba(255,255,255,0.06));
  }

  .brush-accent {
    position: absolute;
    left: 463px; top: 245px; width: 259px; height: 167px;
    background: radial-gradient(ellipse at 85% 85%, rgba(166,127,85,0.35), rgba(166,127,85,0) 70%);
  }

  .brand-name {
    position: absolute;
    font-weight: 400;
    letter-spacing: 0.06em;
    white-space: nowrap;
    text-align: right;
  }
  .card--front .brand-name {
    right: 40px; top: 78px;
    font-size: 34px;
    color: var(--sage);
  }
  .card--back .brand-name {
    right: 45px; top: 290px;
    font-size: 38px;
    color: var(--card-white);
  }

  .holder-name {
    position: absolute;
    left: 42px; top: 226px;
    font-size: 47px;
    font-weight: 700;
    color: var(--sage);
    letter-spacing: -0.01em;
  }
  .contact-list {
    position: absolute;
    left: 40px; top: 290px;
    list-style: none;
  }
  .contact-list li {
    display: flex;
    align-items: center;
    height: 30px;
    font-size: 20px;
    color: var(--ink);
  }
  .contact-list svg {
    width: 16px; height: 16px;
    margin-right: 10px;
    fill: var(--gold);
    flex-shrink: 0;
  }
</style>
</head>
<body>
  <section class="card card--front">
    <div class="sprig" role="img" aria-label="Hand-drawn leafy sprig illustration in sage green"></div>
    <div class="brush-accent" role="img" aria-label="Soft gold brushstroke sweep"></div>
    <div class="brand-name">Wrenfield Acres</div>
    <h1 class="holder-name">Danielle Hoskins</h1>
    <ul class="contact-list">
      <li>
        <svg viewBox="0 0 24 24" aria-hidden="true"><path d="M6.6 2.5c.6-.3 1.3-.1 1.6.5l2 3.6c.3.6.2 1.2-.3 1.6L8.4 9.5c1 2.4 3.1 4.6 5.6 5.7l1.4-1.5c.4-.5 1.1-.6 1.6-.3l3.6 2c.6.3.8 1 .5 1.6l-1.2 2.4c-.4.8-1.3 1.3-2.2 1.1C10.3 19.3 4.7 13.7 3.6 6.3c-.1-.9.3-1.8 1.1-2.2z"/></svg>
        30.412.6638
      </li>
      <li>
        <svg viewBox="0 0 24 24" aria-hidden="true"><path d="M2 6h20v12H2z"/><path d="M3 7l9 6.2L21 7" stroke="#fff" stroke-width="1.6" fill="none"/></svg>
        danielle@wrenfieldacres.com
      </li>
      <li>
        <svg viewBox="0 0 24 24" aria-hidden="true"><path d="M12 2a7 7 0 0 0-7 7c0 5 7 13 7 13s7-8 7-13a7 7 0 0 0-7-7zm0 9.5a2.5 2.5 0 1 1 0-5 2.5 2.5 0 0 1 0 5z"/></svg>
        2716 Wrenfield Rd, Fernbrook, CO 80742
      </li>
    </ul>
  </section>

  <section class="card card--back">
    <div class="sprig" role="img" aria-label="Hand-drawn leafy sprig illustration in white line work"></div>
    <div class="brand-name">Wrenfield Acres</div>
  </section>
</body>
</html>
```